Pitch book for Birchmere Property Partners.

Birchmere Partners is a new real estate investment company focused on multifamily (apartment) investments along the San Francisco Peninsula (in other parts of the world it is also referred to as flats). We need a professional Pitch Book i.e. brochure (digital and print) to raise equity from private investors. Read about “pitch book” on Lexipedia. The profile of the investor is conservative and must qualify as an accredited investor. Think high net worth individuals, CEOs and wealthy retiring couples. The investor that is attracted to real estate invest because it is low risk, produce cash flow and provide solid returns over the long term.

The brochure should convey trust, be highly professional and be clean and crisp. I attach a PowerPoint doc to be used as a copy for the brochure. I also attach a brochure of Halvert Crane – I like the look and feel, think it was designed with InDesign.

We will use the brochure at one-on-one meetings with investors where we will present on a laptop; we also need it in a format so that we can email it, print it and use it to be uploaded as a website.

I prefer the up and down scroll format (like you would do on a Mac) compared to PowerPoint but I am open to suggestions.

The photos I used in the PowerPoint presentation was found on the web, please use your own stock images.

Target Market(s)

High net worth individuals

Industry/Entity Type

Real Estate

Font styles to use
Serif

Requirements
Must have
• See attached Power Point
Nice to have
• See attached HVC brochure, I like the look and feel.
Should not have
• I am open to your ideas.

```html
<!DOCTYPE html>
<html lang="en">
<head>
<meta charset="utf-8">
<title>Birchmere Property Partners — San Francisco Peninsula Pitch Book</title>
<link rel="stylesheet" href="https://fonts.googleapis.com/css2?family=EB+Garamond:wght@400;500&display=swap">
<style>
  :root {
    --backdrop: #a9a9a9;
    --paper: #f7f7f7;
    --ink: #2b2b2b;
    --ink-soft: #4a4a4a;
    --sky-top: #2b1fb8;
    --sky-mid: #4a35d0;
    --sky-glow: #9a6fd6;
    --horizon: #d98aa8;
    --water: #2a2a7a;
  }
  * { margin: 0; padding: 0; box-sizing: border-box; }
  html, body {
    width: 1200px;
    height: 908px;
    overflow: hidden;
  }
  body {
    background: var(--backdrop);
    font-family: "EB Garamond", Garamond, "Times New Roman", serif;
    display: flex;
    align-items: center;
    justify-content: center;
  }
  .cover {
    width: 1000px;
    height: 700px;
    background: var(--paper);
    display: flex;
    flex-direction: column;
    box-shadow: 0 2px 6px rgba(0,0,0,0.15);
  }
  .cover-photo {
    height: 462px;
    background:
      linear-gradient(180deg,
        var(--sky-top) 0%,
        var(--sky-mid) 38%,
        var(--sky-glow) 58%,
        var(--horizon) 66%,
        #3b2f8a 72%,
        var(--water) 100%);
  }
  .cover-band {
    flex: 1;
    position: relative;
    padding: 0 60px;
  }
  .cover-title {
    position: absolute;
    left: 60px;
    bottom: 58px;
    color: var(--ink);
    text-transform: uppercase;
  }
  .cover-title .place {
    font-size: 27px;
    font-weight: 500;
    letter-spacing: 0.04em;
    line-height: 1.1;
  }
  .cover-title .subject {
    font-size: 21px;
    font-weight: 400;
    letter-spacing: 0.12em;
    color: var(--ink-soft);
    margin-top: 4px;
  }
  .brand {
    position: absolute;
    right: 60px;
    top: 34px;
    display: flex;
    flex-direction: column;
    align-items: center;
    gap: 10px;
    color: var(--ink);
  }
  .brand-mark {
    width: 38px;
    height: 38px;
    background: var(--ink);
  }
  .brand-name {
    font-size: 18px;
    font-weight: 500;
    letter-spacing: 0.08em;
    text-transform: uppercase;
  }
</style>
</head>
<body>
  <main class="cover">
    <div class="cover-photo" role="img" aria-label="Photograph of a suspension bridge lit at dusk over the bay, with the city skyline under a violet sky"></div>
    <section class="cover-band">
      <div class="brand">
        <span class="brand-mark"></span>
        <span class="brand-name">Birchmere</span>
      </div>
      <h1 class="cover-title">
        <span class="place">San Francisco Peninsula</span>
        <div class="subject">Multifamily Real Estate Investment</div>
      </h1>
    </section>
  </main>
</body>
</html>
```